Letterhead and Stationary for Construction Company

Brisk Current needs modern Letterhead, Envelopes and Notepad designs.

Industry/Entity Type

Construction

Colors
f78f20
34a7d8
ffffff

Requirements
Must have
• Modern looking design.

```html
<!DOCTYPE html>
<html lang="en">
<head>
<meta charset="utf-8">
<title>Brisk Current Stationery</title>
<link rel="stylesheet" href="https://fonts.googleapis.com/css2?family=Arimo:wght@400;700&family=Varela+Round&display=swap">
<style>
:root{
  --orange:#f47b2a;
  --blue:#2f6fc0;
  --navy:#2f4aa6;
  --sky:#16a6e4;
  --paper:#ffffff;
  --stage:#ececec;
  --ink:#333333;
}
*{margin:0;padding:0;box-sizing:border-box}
html,body{width:1200px;height:938px;overflow:hidden}
body{background:var(--stage);position:relative;font-family:"Arimo",Arial,sans-serif;color:var(--ink)}
.sheet{position:absolute;background:var(--paper);overflow:hidden}
.band{position:absolute;left:0;bottom:0;width:100%;background:linear-gradient(90deg,var(--navy),var(--sky) 55%,var(--navy))}
.brand{position:absolute;display:flex;align-items:center;gap:6px;font-family:"Varela Round",Arial,sans-serif;color:var(--blue);white-space:nowrap;line-height:1}
.brand .dot{border-radius:50%;background:var(--orange);flex:none}

/* letterhead */
.letterhead{left:184px;top:68px;width:386px;height:544px}
.letterhead .brand{left:18px;top:30px;font-size:17px}
.letterhead .brand .dot{width:16px;height:16px}
.letterhead .band{height:56px}
.contact{position:absolute;right:20px;top:23px;text-align:right;font-size:4.6px;line-height:7.3px;color:#222}
.contact .icon{display:inline-block;width:4px;height:4px;background:var(--navy);border-radius:1px;margin-left:2px;vertical-align:-0.5px}
.letter{position:absolute;left:37px;top:138px;width:300px;font-size:5.3px;line-height:8.4px;color:#444}
.letter p{margin-bottom:8px}
.letter .gap{margin-bottom:24px}
.letter strong{color:#222}
.signature{width:40px;height:26px;background:#e7e7e7;margin:4px 0 6px}

/* notepad */
.notepad{left:636px;top:40px;width:458px;height:576px}
.notepad .brand{left:150px;top:262px;font-size:27px;gap:9px}
.notepad .brand .dot{width:26px;height:26px}
.notepad .band{height:62px}

/* cards */
.card{border-radius:8px}
.card-front{left:46px;top:660px;width:175px;height:98px}
.card-front .brand{right:14px;top:14px;font-size:13px;gap:4px}
.card-front .brand .dot{width:13px;height:13px}
.card-front .band{height:50px}
.card-front .holder{position:absolute;left:11px;top:60px;color:#fff;font-size:5.4px;line-height:6.2px}
.card-front .holder .name{font-weight:700;font-size:5.8px}
.card-front .holder .addr{margin-top:7px;font-size:4.4px;line-height:5.4px}
.card-front .lines{position:absolute;right:9px;top:59px;color:#fff;font-size:3.4px;line-height:6.2px;text-align:right}
.card-back{left:46px;top:786px;width:176px;height:99px}
.card-back .brand{left:40px;top:40px;font-size:15px;gap:5px}
.card-back .brand .dot{width:14px;height:14px}

/* envelopes */
.envelope{left:266px;top:674px;width:433px;height:208px}
.envelope .brand{left:15px;top:25px;font-size:15px;gap:5px}
.envelope .brand .dot{width:15px;height:15px}
.envelope .band{height:58px}
.envelope-back{left:737px;top:672px;width:432px;height:208px}
.flap{position:absolute;left:0;top:0;width:100%;height:72px;border-radius:0 0 34px 34px;background:linear-gradient(90deg,var(--navy),var(--sky) 55%,var(--navy));display:flex;align-items:center;justify-content:center}
.flap .web{color:#fff;font-size:10.5px;letter-spacing:3px;margin-top:-10px}
</style>
</head>
<body>

<!-- Letterhead -->
<section class="sheet letterhead">
  <div class="brand"><span class="dot"></span>Brisk Current</div>
  <div class="contact">
    12 Riverside Way, Floor 3<br>Northgate District<br>
    020 555 0142<span class="icon"></span><br>
    020 555 0142<span class="icon"></span><br>
    020 555 0142<span class="icon"></span><br>
    hello@briskcurrent.com<span class="icon"></span><br>
    www.briskcurrent.com<span class="icon"></span>
  </div>
  <div class="letter">
    <p>July 2, 2012</p>
    <p><strong>Dear CH,</strong><br>Unit 4 Kestrel Park, Millbrook</p>
    <p class="gap">Thank you for choosing our team for the new office block on Harbor Street. This letter confirms the schedule we agreed during our site meeting last week. Ground works will begin at the start of next month, followed by the steel frame and the roof. Our site manager will send weekly progress notes and photos, and will be your first contact for any question. We will keep noise and traffic to a minimum and follow every safety rule on site.</p>
    <p class="gap">Please find the signed contract and the first invoice enclosed with this letter for your records and review.</p>
    <p>Should your plans change, simply let us know and we will adjust the programme with you. Our design office can also help with fit-out, lighting and heating once the shell is complete. We value long partnerships and look forward to building many more projects together with your company in the coming years. Thank you again for your trust and your kind support.</p>
    <p>Best Regards,</p>
    <div class="signature" role="img" aria-label="Handwritten signature"></div>
    <p><strong>Laura Finch</strong><br>Director</p>
    <p>Unit 4 Kestrel Park, Millbrook</p>
  </div>
  <div class="band" role="img" aria-label="Decorative orange and blue footer band"></div>
</section>

<!-- Notepad -->
<section class="sheet notepad">
  <div class="brand"><span class="dot"></span>Brisk Current</div>
  <div class="band" role="img" aria-label="Decorative orange and blue footer band"></div>
</section>

<!-- Business card front -->
<section class="sheet card card-front">
  <div class="brand"><span class="dot"></span>Brisk Current</div>
  <div class="band" role="img" aria-label="Decorative orange and blue band"></div>
  <div class="holder">
    <div class="name">DANIEL MOORE</div>
    <div>Managing Director</div>
    <div class="addr">12 Riverside Way<br>Northgate District</div>
  </div>
  <div class="lines">020 555 0142<br>020 555 0142<br>020 555 0142<br>hello@briskcurrent.com<br>www.briskcurrent.com</div>
</section>

<!-- Business card back -->
<section class="sheet card card-back">
  <div class="brand"><span class="dot"></span>Brisk Current</div>
</section>

<!-- Envelope front -->
<section class="sheet envelope">
  <div class="brand"><span class="dot"></span>Brisk Current</div>
  <div class="band" role="img" aria-label="Decorative orange and blue footer band"></div>
</section>

<!-- Envelope back -->
<section class="sheet envelope-back">
  <div class="flap"><span class="web">www.briskcurrent.com</span></div>
</section>

</body>
</html>
```